Business Card Design

We would like a business card that utilizes our current logo and keeps with the same feel - elegant and organic. Our farm isn't about mass production, it's about excellence, education, beautiful events and flowers - people, culture, and community.

Target Market(s)

Patrons to our farm who are interested in weddings, events, or our flowers and vegetables.

Contact Information for Business Card

Name, address, cell email (Danielle Hoskins, 2716 Wrenfield Rd, Fairhollow, CO 80519, cell 30.412.6638, email danielle@wrenfieldacres.com)

```html
<!DOCTYPE html>
<html lang="en">
<head>
<meta charset="utf-8">
<title>Wrenfield Acres – Business Card</title>
<link rel="stylesheet" href="https://fonts.googleapis.com/css2?family=Roboto:wght@400;500&display=swap">
<style>
  :root {
    --page: #ffffff;
    --card-front: #ffffff;
    --card-back: #768873;
    --sage: #73866f;
    --sage-deep: #66785f;
    --bronze: #a37a4c;
    --ink: #222222;
  }
  * { margin: 0; padding: 0; box-sizing: border-box; }
  html, body {
    width: 1200px; height: 896px; overflow: hidden;
    background: var(--page);
    font-family: "Roboto", Arial, sans-serif;
  }
  .canvas { position: relative; width: 1200px; height: 896px; }

  .card {
    position: absolute; left: 334px; width: 529px; height: 303px;
    border-radius: 26px; overflow: hidden;
  }
  .card--front { top: 124px; background: var(--card-front); border: 1px solid #e6e6e6; }
  .card--back { top: 472px; background: var(--card-back); }

  .brand {
    position: absolute; left: 20px; top: 42px;
    display: flex; align-items: center; gap: 12px;
    color: var(--sage); font-weight: 500; font-size: 34px; letter-spacing: 0.5px;
  }
  .brand__dot { width: 14px; height: 14px; border-radius: 50%; background: var(--sage); }

  .details {
    position: absolute; left: 331px; top: 117px; height: 165px;
    border-left: 1.5px solid var(--bronze); padding-left: 13px;
    color: var(--ink);
  }
  .details__name { color: var(--bronze); font-weight: 500; font-size: 23px; line-height: 1; margin-top: -1px; }
  .details__role { font-size: 12px; margin-top: 5px; }
  .details__address { font-size: 11.5px; line-height: 20px; margin-top: 20px; white-space: nowrap; }
  .details__contacts { list-style: none; margin-top: 10px; font-size: 12px; }
  .details__contacts li { display: flex; align-items: center; gap: 4px; height: 20px; }
  .icon { width: 10px; height: 10px; fill: var(--bronze); flex: none; }

  .back-mark {
    position: absolute; inset: 0;
    display: flex; align-items: center; justify-content: center;
    color: var(--sage-deep); font-weight: 500; font-size: 52px; letter-spacing: 1px;
  }
</style>
</head>
<body>
<main class="canvas">
  <section class="card card--front" aria-label="Business card front">
    <div class="brand"><span class="brand__dot"></span><span>Wrenfield Acres</span></div>
    <div class="details">
      <p class="details__name">Owen Harlow</p>
      <p class="details__role">Managing Director</p>
      <p class="details__address">Danielle Hoskins, 2716 Wrenfield<br>Rd, Fairhollow, CO 80519</p>
      <ul class="details__contacts">
        <li>
          <svg class="icon" viewBox="0 0 10 10"><path d="M2.5 0h5a1 1 0 0 1 1 1v8a1 1 0 0 1-1 1h-5a1 1 0 0 1-1-1V1a1 1 0 0 1 1-1zm.3 1.2v6.6h4.4V1.2z"/></svg>
          30.412.6638
        </li>
        <li>
          <svg class="icon" viewBox="0 0 10 10"><path d="M0 2h10v.8L5 5.6 0 2.8zM0 3.8l5 2.8 5-2.8V8H0z"/></svg>
          info@wrenfieldacres.com
        </li>
        <li>
          <svg class="icon" viewBox="0 0 10 10"><circle cx="5" cy="5" r="5"/><path d="M3 2.2c1 .3 1.2 1.3.5 2s.4 1.8 1.4 1.6M6.5 1.2c-.4 1 .3 1.6 1.3 1.5M6 8.8c.2-1 1-1.3 1.9-1.3" stroke="#fff" stroke-width=".8" fill="none"/></svg>
          www.wrenfieldacres.com
        </li>
      </ul>
    </div>
  </section>

  <section class="card card--back" aria-label="Business card back">
    <div class="back-mark">Wrenfield Acres</div>
  </section>
</main>
</body>
</html>
```